Children's Educational Software - Login Screens

We need graphics for some basic login pages. The main requirements are a background image, buttons and background overlay (box for login fields and app icons). Must utilize responsive design for various resolutions and devices. The mock-up file provides an example of the direction we are wanting to go. The app page will require a version of the background that extends down using a solid colour. One idea would be to add some flowers, bees, etc. to help add some life to the bottom half. I like the idea of clouds and grass, but am open to anything.

Target Market(s)

Elementary teachers and young children

Coding

Coded - Design and coding required

Number of Pages Required

2 page

Font styles to use
Sans Serif

Requirements
Must have
• Responsive design for various resolutions and devices
Nice to have
• clouds, grass, new app icons if current icons don't fit with new design

```html
<!DOCTYPE html>
<html lang="en">
<head>
<meta charset="UTF-8">
<title>BrightSteps – School Login</title>
<link href="https://fonts.googleapis.com/css2?family=Roboto:wght@400;500;700&display=swap" rel="stylesheet">
<style>
  :root {
    --sky: #cdf3fd;
    --mountain: #5ea9fb;
    --grass: #77c100;
    --grass-dark: #5aa000;
    --brand: #1f3c88;
    --header: #00aef5;
    --text: #1e3f8a;
    --field: #f2f2f2;
    --tile-top: #3aa3e4;
    --tile-bottom: #3ccbea;
    --white: #ffffff;
  }
  * { box-sizing: border-box; margin: 0; padding: 0; }
  html, body { width: 1200px; height: 675px; overflow: hidden; }
  body { font-family: 'Roboto', sans-serif; color: var(--text); position: relative; background: var(--sky); }

  .scenery {
    position: absolute; inset: 0;
    background: linear-gradient(180deg, var(--sky) 0%, var(--sky) 45%, #a9d7fc 62%, var(--mountain) 76%, var(--grass) 90%, var(--grass-dark) 100%);
  }

  .brand {
    position: absolute; left: 52px; top: 50px;
    display: flex; align-items: center; gap: 14px;
  }
  .brand-mark { width: 22px; height: 22px; background: var(--header); border-radius: 3px; }
  .brand-name { font-size: 44px; font-weight: 500; color: var(--brand); letter-spacing: -0.5px; line-height: 1; }

  .login-card {
    position: absolute; left: 387px; top: 148px; width: 426px; height: 378px;
    background: var(--white); border-radius: 2px;
    box-shadow: 0 2px 6px rgba(30, 63, 138, 0.12);
    overflow: hidden;
  }
  .login-header {
    height: 55px; background: var(--header);
    display: flex; align-items: center; justify-content: center;
  }
  .login-title { color: var(--white); font-size: 25px; font-weight: 700; }

  .login-body { padding: 12px 47px 0; }
  .field-label { display: block; font-size: 14px; margin-bottom: 9px; }
  .field-input {
    display: block; width: 332px; height: 42px; border: 0; border-radius: 2px;
    background: var(--field); font: inherit;
  }
  .option { display: flex; align-items: center; gap: 6px; margin-top: 23px; font-size: 14px; }
  .option-box { width: 21px; height: 21px; background: var(--field); border-radius: 2px; }

  .role-list { display: flex; gap: 24px; margin-top: 29px; }
  .role-tile {
    width: 95px; height: 94px; border-radius: 2px; overflow: hidden;
    box-shadow: 0 0 0 1px #e4e8ee;
    display: flex; flex-direction: column;
  }
  .role-icon {
    height: 65px; background: linear-gradient(180deg, var(--tile-top), var(--tile-bottom));
    display: flex; align-items: center; justify-content: center;
  }
  .role-icon svg { width: 46px; height: 46px; fill: none; stroke: var(--white); stroke-width: 2.4; stroke-linecap: round; stroke-linejoin: round; }
  .role-label {
    flex: 1; background: var(--field); display: flex; align-items: center; justify-content: center;
    font-size: 14.5px;
  }

  .help-links {
    margin-top: 27px; display: flex; justify-content: center; align-items: center; gap: 9px; font-size: 14px;
  }
  .help-links .divider { width: 1px; height: 15px; background: var(--text); }
</style>
</head>
<body>
  <div class="scenery" role="img" aria-label="Illustrated landscape of clouds, a blue mountain, green hills with trees and a winding river"></div>

  <div class="brand">
    <span class="brand-mark"></span>
    <span class="brand-name">BrightSteps</span>
  </div>

  <main class="login-card">
    <header class="login-header"><h1 class="login-title">School Login</h1></header>
    <div class="login-body">
      <label class="field-label" for="school-id">School ID</label>
      <input class="field-input" id="school-id" type="text">

      <div class="option"><span class="option-box"></span><span>Pick students from a list</span></div>

      <div class="role-list">
        <div class="role-tile">
          <div class="role-icon">
            <svg viewBox="0 0 48 48">
              <circle cx="19" cy="13" r="7"/>
              <path d="M6 40c0-8 6-14 13-14 2 0 4 .5 5.5 1.3"/>
              <path d="M6 40h14"/>
              <circle cx="35" cy="32" r="3"/>
              <circle cx="35" cy="32" r="7.5" stroke-dasharray="3.5 2.4"/>
            </svg>
          </div>
          <div class="role-label">Admin</div>
        </div>
        <div class="role-tile">
          <div class="role-icon">
            <svg viewBox="0 0 48 48">
              <circle cx="24" cy="9" r="4"/>
              <path d="M17 23c0-5 3-8 7-8s7 3 7 8"/>
              <path d="M9 24h30"/>
              <circle cx="12" cy="35" r="3.5"/>
              <circle cx="24" cy="35" r="3.5"/>
              <circle cx="36" cy="35" r="3.5"/>
            </svg>
          </div>
          <div class="role-label">Teacher</div>
        </div>
        <div class="role-tile">
          <div class="role-icon">
            <svg viewBox="0 0 48 48">
              <path d="M3 19l21-10 21 10-21 10z"/>
              <path d="M12 24v10c4 5 20 5 24 0V24"/>
              <path d="M42 21v12"/>
              <circle cx="42" cy="35" r="1.5"/>
            </svg>
          </div>
          <div class="role-label">Student</div>
        </div>
      </div>

      <nav class="help-links">
        <span>Quick start guide</span>
        <span class="divider"></span>
        <span>Support page</span>
      </nav>
    </div>
  </main>
</body>
</html>
```